Business Cards and Logo needed for Rum Website

I need a smart, modern but fun business card (and Logo) to help promote my website BrightBarrelNote.com

The website contains reviews of Rum (and eventually other spirits) as well as news and blog posts.

I would like a 2-sided design, with the logo and company name on one side and text on the other.

Text fields required are:
Name (Dan Wheeler)
Website (www.brightbarrelnote.com)
Email (dan@brightbarrelnote.com)
Twitter (@BrightBarrelNote)

For the logo i'm open to suggestions however it must incorporate a wooden Cask and a number of Stars. Ideas so far have been for a Cask surrounded in a number of Stars forming a circle around it with the text Bright Barrel Note underneath. The logo should be modern but also a little bit cartoony and stylised. General drink/spirits themes will also be considered.

Colours: I like the idea of yellow text with black background but again i'm open to suggestions on what would work well. Contrasting colours for the 2-sides would be good.

Cards will be printed via Printlo.com so please consult their style guidelines if required: http://uk.printlo.com/help/faq/templates-and-guidelines.html

Requirements
Must have
• A spirits Cask
A number of Stars (preferrably yellow or gold)

```html
<!DOCTYPE html>
<html lang="en">
<head>
<meta charset="utf-8">
<title>Bright Barrel Note — Business Card</title>
<link href="https://fonts.googleapis.com/css2?family=Lato:wght@400;700;900&display=swap" rel="stylesheet">
<style>
  :root {
    --backdrop: #95a2a6;
    --card: #ffffff;
    --card-shadow: rgba(0, 0, 0, 0.85);
    --ink: #1a1a1a;
    --mark: #8a5a4a;
  }
  * { margin: 0; padding: 0; box-sizing: border-box; }
  html, body {
    width: 1200px; height: 900px; overflow: hidden;
    background: var(--backdrop);
    font-family: "Lato", sans-serif;
    color: var(--ink);
  }
  .stage { position: relative; width: 1200px; height: 900px; }
  .card {
    position: absolute; top: 147px;
    width: 369px; height: 564px;
    background: var(--card);
    border-radius: 42px;
    box-shadow: 6px 6px 3px var(--card-shadow);
  }
  .card--front { left: 207px; }
  .card--back { left: 628px; }

  .brand { position: absolute; display: flex; align-items: center; }
  .brand__dot { border-radius: 50%; background: var(--mark); flex: none; }
  .brand__name { font-weight: 900; line-height: 1.02; color: var(--ink); }

  .card--front .brand { left: 66px; top: 200px; gap: 22px; }
  .card--front .brand__dot { width: 96px; height: 96px; }
  .card--front .brand__name { font-size: 30px; }

  .website {
    position: absolute; left: 0; right: 0; top: 368px;
    text-align: center; font-size: 21px; font-weight: 400;
  }

  .card--back .brand { right: 42px; top: 248px; gap: 12px; }
  .card--back .brand__dot { width: 56px; height: 56px; }
  .card--back .brand__name { font-size: 17px; }

  .contact { position: absolute; right: 41px; top: 400px; text-align: right; }
  .contact__name { font-size: 23px; font-weight: 700; margin-bottom: 20px; }
  .contact__line {
    display: flex; justify-content: flex-end; align-items: center;
    gap: 10px; font-size: 20px; line-height: 27px;
  }
  .contact__icon { width: 14px; height: 12px; flex: none; }
  .contact__square { width: 9px; height: 9px; background: var(--ink); flex: none; }
</style>
</head>
<body>
<div class="stage">
  <section class="card card--front">
    <div class="brand">
      <span class="brand__dot"></span>
      <span class="brand__name">Bright<br>Barrel<br>Note</span>
    </div>
    <p class="website">www.brightbarrelnote.com</p>
  </section>

  <section class="card card--back">
    <div class="brand">
      <span class="brand__dot"></span>
      <span class="brand__name">Bright<br>Barrel<br>Note</span>
    </div>
    <div class="contact">
      <p class="contact__name">Dan Wheeler</p>
      <p class="contact__line">
        <svg class="contact__icon" viewBox="0 0 14 12" aria-hidden="true">
          <rect x="0.5" y="1.5" width="13" height="9" fill="none" stroke="#1a1a1a" stroke-width="1.4"/>
          <path d="M0.5 1.5 L7 7 L13.5 1.5" fill="none" stroke="#1a1a1a" stroke-width="1.4"/>
        </svg>
        <span>dan@brightbarrelnote.com</span>
      </p>
      <p class="contact__line">
        <span class="contact__square"></span>
        <span>@BrightBarrelNote</span>
      </p>
    </div>
  </section>
</div>
</body>
</html>
```